Business Card Design Wenda Style

I make Hand Made Name necklaces which are known as Wenda Style and would like a Shiny Gold Business Card almost to look like a Gold Bar.
on the 2nd side I want an image of a Wenda Necklace in Silver as it will be on a Gold Background.

Industry/Entity Type

Business

Contact Information for Business Card

Dunvok Jewellery UK
Loop Pendants 2 Go

Hugo Penwright
Director
M: 07700 914 263

www.dunvokjwl.co.uk

Requirements
Must have
• Writing must be in Black

Card must be metallic gold

```html
<!DOCTYPE html>
<html lang="en">
<head>
<meta charset="utf-8">
<title>Dunvok Jewellery UK – Business Card</title>
<link rel="stylesheet" href="https://fonts.googleapis.com/css2?family=Open+Sans:wght@400;700&display=swap">
<style>
  :root {
    --bg: #ece8e2;
    --ink: #1d1a16;
    --gold-dark: #8c5c1b;
    --gold-mid: #c8962f;
    --gold-light: #f4e6b8;
    --gold-warm: #d9ab44;
    --silver-dark: #b9b9b6;
    --silver-light: #f7f7f4;
    --card-edge: #1a1a1a;
  }
  * { margin: 0; padding: 0; box-sizing: border-box; }
  html, body {
    width: 1200px; height: 1000px; overflow: hidden;
    background: var(--bg);
    font-family: "Open Sans", Arial, sans-serif;
    color: var(--ink);
  }
  .stage {
    position: relative; width: 1200px; height: 1000px;
    display: flex; flex-direction: column; align-items: center; justify-content: center; gap: 60px;
  }
  .card {
    position: relative; width: 640px; height: 390px;
    border-radius: 30px;
    background: linear-gradient(115deg, var(--gold-dark) 0%, var(--gold-mid) 28%, var(--gold-light) 50%, var(--gold-warm) 70%, var(--gold-dark) 100%);
    box-shadow: 0 6px 0 var(--card-edge), 0 14px 28px rgba(0,0,0,0.25);
    overflow: hidden;
  }
  .card-front .necklace-visual {
    position: absolute; left: 0; top: 70px; width: 640px; height: 220px;
    background: linear-gradient(180deg, var(--silver-light) 0%, var(--silver-dark) 100%);
    opacity: 0.85;
    border-radius: 110px 20px 110px 20px;
  }
  .brand-block {
    position: absolute; top: 88px; left: 0; right: 0; text-align: center;
  }
  .brand-name {
    font-weight: 700; font-size: 30px; letter-spacing: 0.5px; line-height: 1.2;
  }
  .brand-tagline {
    font-weight: 400; font-size: 36px; line-height: 1.2;
  }
  .contact {
    position: absolute; right: 34px; top: 200px; text-align: right;
    font-size: 17px; line-height: 1.6;
  }
  .contact-line { display: flex; align-items: center; justify-content: flex-end; gap: 6px; }
  .contact-line svg { width: 13px; height: 13px; }
  .person {
    position: absolute; left: 40px; bottom: 40px;
  }
  .person-name { font-weight: 700; font-size: 30px; line-height: 1.2; }
  .person-role { font-weight: 400; font-size: 28px; line-height: 1.2; }
</style>
</head>
<body>
<main class="stage">
  <section class="card card-front">
    <div class="necklace-visual" role="img" aria-label="Silver Wenda Style name necklace on a fine chain"></div>
  </section>

  <section class="card card-back">
    <div class="brand-block">
      <p class="brand-name">DUNVOK JEWELLERY</p>
      <p class="brand-tagline">UK LOOP PENDANTS 2 GO</p>
    </div>

    <div class="contact">
      <p class="contact-line">07700 914 263
        <svg viewBox="0 0 16 16" aria-hidden="true"><rect x="4" y="1" width="8" height="14" rx="1.5" fill="none" stroke="currentColor" stroke-width="1.4"/><circle cx="8" cy="12.5" r="0.9" fill="currentColor"/></svg>
      </p>
      <p class="contact-line">www.dunvokjwl.co.uk
        <svg viewBox="0 0 16 16" aria-hidden="true"><circle cx="8" cy="8" r="6.5" fill="none" stroke="currentColor" stroke-width="1.3"/><ellipse cx="8" cy="8" rx="3" ry="6.5" fill="none" stroke="currentColor" stroke-width="1.1"/><line x1="1.5" y1="8" x2="14.5" y2="8" stroke="currentColor" stroke-width="1.1"/></svg>
      </p>
    </div>

    <div class="person">
      <p class="person-name">Hugo Penwright</p>
      <p class="person-role">Director</p>
    </div>
  </section>
</main>
</body>
</html>
```